Dentistry

Dentist's personal business card. No logo needed. The card shoul deliver the massage of reliability, professionalism, experience.
Please ad the full brief of the project: down the line it says: the winning look should be precise and pristine NO pictures of Teeth, smiles, instruments etc.

The details to be desplaid are:
Dr. Lev Oranbury
Doctor of Dental Surgery
PHD
Web. Www.droranbury.example
Email. Lev@droranbury.example
Tel 07700900318
Surgery address. 27Bfernwick road London SE4 7QX UK
62 Harlow Crescent London EC3V 9PD. Uk

Industry/Entity Type

Massage

Requirements
Should not have
• Logo, teeth, smile any sort of instruments.

```html
<!DOCTYPE html>
<html lang="en">
<head>
<meta charset="utf-8">
<title>Dr. Lev Oranbury – Business Card</title>
<link rel="stylesheet" href="https://fonts.googleapis.com/css2?family=Montserrat:wght@400;600;700&display=swap">
<style>
  :root {
    --canvas-grey: #e6e7e9;
    --card-white: #ffffff;
    --brand-blue: #1b7db8;
    --brand-blue-dark: #156a9f;
    --brand-blue-light: #8cc6ea;
    --ink: #2d2d2d;
    --shadow: rgba(0, 0, 0, 0.35);
  }
  * { box-sizing: border-box; margin: 0; padding: 0; }
  html, body {
    width: 1080px; height: 1200px; overflow: hidden;
    background: var(--canvas-grey);
    font-family: "Montserrat", sans-serif;
  }
  .canvas { position: relative; width: 1080px; height: 1200px; }
  .card {
    position: absolute; width: 904px; height: 502px;
    background: var(--card-white); border-radius: 28px; overflow: hidden;
    box-shadow: 4px 6px 12px var(--shadow);
  }
  .card--front { left: 68px; top: 56px; }
  .card--back { left: 74px; top: 625px; }
  .card__waves { position: absolute; inset: 0; width: 100%; height: 100%; }

  .doctor { position: absolute; left: 76px; top: 142px; }
  .doctor__name { color: var(--brand-blue); font-weight: 700; font-size: 29px; line-height: 1.1; }
  .doctor__title { color: var(--ink); font-size: 23px; line-height: 1.2; margin-top: 8px; }
  .doctor__phone {
    display: flex; align-items: center; gap: 6px;
    margin-top: 24px; color: var(--ink); font-size: 30px;
  }
  .doctor__phone svg { width: 24px; height: 24px; }

  .contact { position: absolute; left: 500px; top: 146px; }
  .contact__row { display: flex; align-items: center; gap: 14px; color: var(--ink); font-size: 23px; line-height: 1.4; }
  .contact__row svg { width: 24px; height: 24px; flex: none; }

  .addresses {
    position: absolute; right: 93px; top: 384px;
    color: var(--card-white); font-weight: 700; font-size: 22px; line-height: 1.45;
    text-align: right;
  }
  .addresses__row { display: flex; align-items: center; justify-content: flex-end; gap: 16px; }
  .addresses__row svg { width: 24px; height: 20px; }

  .appointment__heading {
    position: absolute; left: 111px; top: 64px;
    color: var(--card-white); font-weight: 600; font-size: 28px;
  }
  .appointment__field {
    position: absolute; left: 105px; display: flex; align-items: baseline; gap: 8px;
    color: var(--brand-blue); font-size: 27px;
  }
  .appointment__field--date { top: 248px; }
  .appointment__field--time { top: 355px; }
  .appointment__line { display: inline-block; width: 470px; border-bottom: 2px solid var(--brand-blue); }
</style>
</head>
<body>
<main class="canvas">

  <section class="card card--front">
    <svg class="card__waves" viewBox="0 0 904 502" preserveAspectRatio="none" aria-hidden="true">
      <path d="M0,375 C160,398 300,372 430,310 C560,248 720,228 904,240 L904,256 C720,244 560,264 430,324 C300,386 160,410 0,390 Z" fill="var(--brand-blue-light)"/>
      <path d="M0,402 C160,420 300,392 430,330 C560,268 720,250 904,268 L904,502 L0,502 Z" fill="var(--brand-blue)"/>
    </svg>

    <div class="doctor">
      <h1 class="doctor__name">Dr. Lev Oranbury</h1>
      <p class="doctor__title">Doctor of Dental Surgery<br>PHD</p>
      <p class="doctor__phone">
        <svg viewBox="0 0 24 24"><path d="M6.6 10.8a15 15 0 0 0 6.6 6.6l2.2-2.2a1 1 0 0 1 1-.25 11.4 11.4 0 0 0 3.6.57 1 1 0 0 1 1 1V20a1 1 0 0 1-1 1A17 17 0 0 1 3 4a1 1 0 0 1 1-1h3.5a1 1 0 0 1 1 1c0 1.25.2 2.45.57 3.57a1 1 0 0 1-.25 1z" fill="var(--brand-blue)"/></svg>
        07700900318
      </p>
    </div>

    <div class="contact">
      <p class="contact__row">
        <svg viewBox="0 0 24 24"><rect x="2" y="5" width="20" height="14" fill="none" stroke="var(--brand-blue)" stroke-width="1.6"/><path d="M2 5l10 8 10-8" fill="none" stroke="var(--brand-blue)" stroke-width="1.6"/></svg>
        Lev@droranbury.example
      </p>
      <p class="contact__row">
        <svg viewBox="0 0 24 24" fill="none" stroke="var(--brand-blue)" stroke-width="1.6"><circle cx="12" cy="12" r="9.5"/><ellipse cx="12" cy="12" rx="4" ry="9.5"/><path d="M2.5 12h19M4 7h16M4 17h16"/></svg>
        www.droranbury.example
      </p>
    </div>

    <div class="addresses">
      <p class="addresses__row">
        <svg viewBox="0 0 26 22"><path d="M2 11c3-5 7-7 11-7s8 2 11 7c-3 5-7 7-11 7S5 16 2 11z" fill="none" stroke="#fff" stroke-width="2"/><circle cx="13" cy="11" r="3.5" fill="#fff"/></svg>
        27Bfernwick road London SE4 7QX UK
      </p>
      <p>62 Harlow Crescent London EC3V 9PD. Uk</p>
    </div>
  </section>

  <section class="card card--back">
    <svg class="card__waves" viewBox="0 0 904 502" preserveAspectRatio="none" aria-hidden="true">
      <path d="M0,0 L904,0 L904,20 C740,16 600,60 480,100 C340,148 180,160 0,140 Z" fill="var(--brand-blue)"/>
      <path d="M0,150 C180,170 340,158 480,112 C600,72 740,30 904,30 L904,40 C740,40 600,82 480,122 C340,168 180,180 0,160 Z" fill="var(--brand-blue-light)"/>
      <path d="M0,166 C180,186 340,173 480,127 C600,87 740,46 904,44" fill="none" stroke="var(--brand-blue-dark)" stroke-width="5"/>
    </svg>

    <h2 class="appointment__heading">Next appointment:</h2>
    <p class="appointment__field appointment__field--date">Date <span class="appointment__line"></span></p>
    <p class="appointment__field appointment__field--time">Time <span class="appointment__line"></span></p>
  </section>

</main>
</body>
</html>
```